VORLANE (PTY)LTD Website design

WEBSITE design based on our different divisions in our organization.
Our company specializes in the following.
Construction
Property development
Demolition
Mining
Transport
Manufacturing of concrete bricks and blocks
Lightweight concrete Readymix
I want a very modern website and look that fits in with our organization and the changing times of the world.
The website must be very professional and crisp and should appeal to both the younger generation and older generation of business leaders and.
The website must be very user friendly and easy to navigate, simple yet modern, professional and corporate.

```html
<!DOCTYPE html>
<html lang="en">
<head>
<meta charset="utf-8">
<title>VORLANE (PTY)LTD</title>
<link href="https://fonts.googleapis.com/css2?family=Roboto:wght@400;500;700;900&display=swap" rel="stylesheet">
<style>
:root{
  --blue:#1a8fd2;
  --blue-dark:#0d5f8f;
  --ink:#111;
  --text:#333;
  --nav:#2b2b2b;
  --line:#d6d6d6;
  --field:#e9e9e9;
}
*{box-sizing:border-box;margin:0;padding:0}
html,body{width:1200px;height:3051px;overflow:hidden;background:#fff}
body{font-family:'Roboto',sans-serif;color:var(--text);position:relative}
.abs{position:absolute}
.blue{color:var(--blue)}

/* top bar */
.topbar{position:absolute;left:0;top:0;width:1200px;height:45px;border-bottom:1px solid #e6e6e6;font-size:11px;color:#444}
.topbar .tag{position:absolute;top:15px;white-space:nowrap}
.topbar .sep{position:absolute;left:393px;top:14px;width:1px;height:14px;background:#ccc}
.social{position:absolute;display:flex;gap:4px}
.social span{width:26px;height:26px;display:block}
.s1{background:#3b5998}.s2{background:#1da1f2}.s3{background:#dd4b39}.s4{background:#0e76a8}

/* header */
.brand{position:absolute;left:173px;top:60px;display:flex;align-items:center;gap:10px}
.brand .mark{width:20px;height:20px;background:var(--blue)}
.brand .name{font-size:36px;font-weight:900;color:var(--blue);letter-spacing:1px;line-height:1}
.contact-item{position:absolute;top:72px;display:flex;gap:10px;font-size:11px;color:#444;line-height:1.35;white-space:nowrap}
.contact-item b{display:block;font-size:12px;color:#111;font-weight:700}
.hdiv{position:absolute;top:74px;width:1px;height:34px;background:#ddd}

/* nav */
.nav{position:absolute;top:134px;left:0;width:1200px;height:39px;background:var(--nav)}
.nav a{position:absolute;top:13px;color:#fff;font-size:12px;font-weight:700;text-decoration:none}
.nav i{position:absolute;top:8px;width:1px;height:23px;background:#4a4a4a}

/* hero */
.hero{position:absolute;top:173px;left:0;width:1200px;height:502px;background:linear-gradient(90deg,#9aa2a8 0%,#c3cdd5 35%,#d9e3ea 60%,#8f97a0 100%)}
.hero-frame{position:absolute;left:146px;top:207px;width:712px;height:57px;border:2px solid rgba(255,255,255,.7)}
.hero h1{position:absolute;left:173px;top:222px;font-size:44px;line-height:1.1;font-weight:900;color:#111;letter-spacing:-.5px;white-space:nowrap}
.hero p{position:absolute;left:173px;top:290px;width:500px;font-size:11.5px;line-height:1.5;color:#fff}
.btn{display:flex;align-items:center;justify-content:center;background:var(--blue);color:#fff;font-weight:700;font-size:12px}
.hero .btn{position:absolute;left:177px;top:354px;width:124px;height:36px}
.hero svg{position:absolute;top:212px}

/* section titles */
.stitle{position:absolute;left:0;width:1200px;text-align:center}
.stitle .box{position:absolute;border:2px solid var(--line)}
.stitle h2{position:relative;font-size:42px;line-height:1.15;font-weight:900;color:var(--ink);letter-spacing:-.5px;display:inline-block;background:#fff;padding:0 12px}
.stitle.dark h2{color:#fff;background:transparent}
.stitle.dark .box{border-color:#777}
.rule{position:absolute;left:50%;transform:translateX(-50%);display:flex;align-items:center;gap:3px}
.rule .l{width:60px;height:1px;background:#aaa}
.rule .sq{width:7px;height:5px;background:var(--blue)}
.rule .sq.k{background:#111}
.dark .rule .sq.k{background:#fff}
.lead{position:absolute;left:173px;width:854px;text-align:center;font-size:10.5px;line-height:1.55;color:#444}

/* about */
.about-img{position:absolute;left:173px;top:871px;width:854px;height:266px;background:linear-gradient(180deg,#cfd9e2 0%,#9aa6b0 45%,#7a8578 75%,#b9bdb9 100%)}
.about-frame{position:absolute;left:91px;top:20px;width:747px;height:222px;border:2px solid rgba(255,255,255,.75)}

/* services */
.services{position:absolute;top:1186px;left:0;width:1200px;height:533px;background:linear-gradient(135deg,#2a2d31 0%,#1c1e21 55%,#33363a 100%)}
.services .panel{position:absolute;left:0;top:43px;width:488px;height:451px;background:var(--blue-dark)}
.services .photo{position:absolute;left:173px;top:89px;width:439px;height:336px;border:3px solid #fff;background:linear-gradient(180deg,#4f9fe0 0%,#7fbbe9 35%,#b86d4c 60%,#6f7a5a 100%)}
.services .photo svg{position:absolute;top:150px}
.svc-title{position:absolute;left:645px;top:83px;width:321px;height:63px}
.svc-title .box{position:absolute;inset:0;border:2px solid #777}
.svc-title h2{position:absolute;left:18px;top:8px;font-size:42px;line-height:1.15;font-weight:900;color:#fff;letter-spacing:-.5px;white-space:nowrap}
.svc-text{position:absolute;left:662px;top:187px;width:370px;font-size:10.5px;line-height:1.5;color:#eee}
.svc-list{position:absolute;left:662px;top:262px;list-style:none}
.svc-list li{display:flex;align-items:center;gap:12px;height:27.5px;color:#fff;font-size:11px;font-weight:700}
.tick{width:16px;height:16px;background:var(--blue);display:flex;align-items:center;justify-content:center}

/* news */
.card{position:absolute;top:1943px;width:268px;height:331px;border:1px solid #e5e5e5;background:#fff}
.card .thumb{height:142px}
.t1{background:linear-gradient(180deg,#9ec3e0 0%,#d8c35a 55%,#8b8478 100%)}
.t2{background:linear-gradient(180deg,#b9d3e8 0%,#6c8fb3 50%,#5d6a78 100%)}
.t3{background:linear-gradient(180deg,#d9dde1 0%,#9aa1a8 50%,#d49a2e 80%,#6a6d70 100%)}
.date{position:absolute;left:6px;top:165px;width:45px;height:45px;background:var(--blue);color:#fff;text-align:center;font-weight:700;line-height:1.05;padding-top:6px}
.date b{display:block;font-size:17px}
.date span{font-size:11px}
.card h3{position:absolute;left:66px;top:172px;width:195px;font-size:12.5px;line-height:1.35;color:#111;font-weight:700}
.card p{position:absolute;left:66px;top:218px;width:190px;font-size:10.5px;line-height:1.62;color:#555}

/* contact */
.contact{position:absolute;top:2349px;left:0;width:1200px;height:645px;background:linear-gradient(180deg,#25282c 0%,#1b1d20 50%,#2c3034 100%)}
.phone-line{position:absolute;top:137px;left:0;width:1200px;text-align:center;font-size:22px;font-weight:700;color:#fff}
.contact .lead{color:#ddd;top:185px}
.field{position:absolute;height:37px;background:var(--field);font-size:10px;color:#999;padding:11px 14px}
.contact .btn{position:absolute;left:508px;top:517px;width:184px;height:43px;font-size:13px}

/* footer */
.footer{position:absolute;top:2994px;left:0;width:1200px;height:57px;background:var(--blue)}
.footer .copy{position:absolute;left:173px;top:22px;font-size:11px;color:#fff}
.footer .social span{border:1.5px solid #fff;background:transparent}
</style>
</head>
<body>

<div class="topbar">
  <span class="tag" style="left:173px">Manufacturing of Concrete Bricks and Blocks</span>
  <i class="sep"></i>
  <span class="tag" style="left:409px">Lightweight Concrete Readymix</span>
  <div class="social" style="left:915px;top:9px"><span class="s1"></span><span class="s2"></span><span class="s3"></span><span class="s4"></span></div>
</div>

<div class="brand"><span class="mark"></span><span class="name">VORLANE</span></div>

<div class="contact-item" style="left:433px">
  <svg width="14" height="18" viewBox="0 0 14 18"><path d="M7 0a7 7 0 0 0-7 7c0 5 7 11 7 11s7-6 7-11a7 7 0 0 0-7-7z" fill="#1a8fd2"/><circle cx="7" cy="7" r="2.6" fill="#fff"/></svg>
  <div><b>ADDRESS</b>Wester Cape / Eastern Cape / KZN / South Africa</div>
</div>
<i class="hdiv" style="left:698px"></i>
<div class="contact-item" style="left:736px">
  <svg width="16" height="16" viewBox="0 0 24 24"><path d="M6.6 10.8a15 15 0 0 0 6.6 6.6l2.2-2.2c.3-.3.7-.4 1-.2 1.1.4 2.3.6 3.6.6.6 0 1 .4 1 1V20c0 .6-.4 1-1 1A17 17 0 0 1 3 4c0-.6.4-1 1-1h3.5c.6 0 1 .4 1 1 0 1.3.2 2.5.6 3.6.1.3 0 .7-.2 1z" fill="#1a8fd2"/></svg>
  <div><b>MOBILE</b>+27 (0) 41 308 7724</div>
</div>
<i class="hdiv" style="left:885px"></i>
<div class="contact-item" style="left:919px">
  <svg width="18" height="16" viewBox="0 0 18 16"><path d="M0 6l9-6 9 6v10H0z" fill="#1a8fd2"/><path d="M2 7l7 5 7-5" stroke="#fff" stroke-width="1.5" fill="none"/></svg>
  <div><b>MAIL</b>info@vorlane.co.za</div>
</div>

<nav class="nav">
  <a style="left:173px">HOME</a><i style="left:258px"></i>
  <a style="left:297px">ABOUT US</a><i style="left:405px"></i>
  <a style="left:445px">SERVICES</a><i style="left:549px"></i>
  <a style="left:590px">NEWS</a><i style="left:671px"></i>
  <a style="left:714px">CONTACT US</a><i style="left:815px"></i>
</nav>

<section class="hero" role="img" aria-label="Two engineers in hard hats and safety vests reviewing plans on a construction site with a crane">
  <div class="hero-frame"></div>
  <h1>VORLANE BUILDING <span class="blue">TOMORROW</span></h1>
  <p>Lorem ipsum dolor sit amet, consectetur adipiscing elit. Mauris dapibus ex sed eros molestie blandit. Fusce sem enim, commodo sit amet diam pharetra, aliquet pulvinar purus.</p>
  <div class="btn">READ MORE</div>
  <svg style="left:32px" width="14" height="26" viewBox="0 0 14 26"><path d="M12 2L2 13l10 11" stroke="#fff" stroke-width="2" fill="none"/></svg>
  <svg style="left:1150px" width="14" height="26" viewBox="0 0 14 26"><path d="M2 2l10 11L2 24" stroke="#fff" stroke-width="2" fill="none"/></svg>
</section>

<div class="stitle" style="top:700px">
  <div class="box" style="left:431px;top:0;width:332px;height:57px"></div>
  <h2 style="top:16px">ABOUT <span class="blue">VORLANE</span></h2>
  <div class="rule" style="top:69px"><i class="l"></i><i class="sq"></i><i class="sq k"></i><i class="sq"></i><i class="l"></i></div>
</div>
<p class="lead" style="top:793px">Lorem Ipsum is simply dummy text of the printing and typesetting industry. Lorem Ipsum has been the industry's standard dummy text ever since the.Lorem Ipsum is simply dummy text of the printing and typesetting industry. Lorem Ipsum has been the industry's standard dummy text ever since the. Lorem Ipsum is simply dummy text of the printing and typesetting industry. Lorem Ipsum has been the industry's standard dummy text ever since the.Lorem Ipsum is simply dummy.</p>

<div class="about-img" role="img" aria-label="Modern glass and concrete office building with trees in front">
  <div class="about-frame"></div>
  <svg class="abs" style="left:800px;top:119px" width="10" height="20" viewBox="0 0 10 20"><path d="M1 1l8 9-8 9" stroke="#fff" stroke-width="2" fill="none"/></svg>
</div>

<section class="services" role="img" aria-label="Dark background of construction blueprints">
  <div class="panel"></div>
  <div class="photo" role="img" aria-label="Brick apartment building under a blue sky">
    <svg style="left:12px" width="26" height="26" viewBox="0 0 26 26"><circle cx="13" cy="13" r="12" fill="rgba(255,255,255,.35)" stroke="#fff" stroke-width="1.5"/><path d="M15 7l-6 6 6 6" stroke="#fff" stroke-width="2" fill="none"/></svg>
    <svg style="left:395px" width="26" height="26" viewBox="0 0 26 26"><circle cx="13" cy="13" r="12" fill="rgba(255,255,255,.35)" stroke="#fff" stroke-width="1.5"/><path d="M11 7l6 6-6 6" stroke="#fff" stroke-width="2" fill="none"/></svg>
  </div>
  <div class="svc-title"><div class="box"></div><h2>OUR <span class="blue">SERVICES</span></h2></div>
  <div class="rule dark" style="top:157px;left:747px;transform:none"><i class="l"></i><i class="sq"></i><i class="sq" style="background:#fff"></i><i class="sq"></i><i class="l"></i></div>
  <p class="svc-text">Lorem Ipsum is not simply random text. It has roots in a piece of classical Latin literature from 45 BC, making it over 2000 years old. Daniel Harrow, a Latin professor at Ashford College in Virginia.</p>
  <ul class="svc-list">
    <li><span class="tick"><svg width="11" height="9" viewBox="0 0 11 9"><path d="M1 4.5l3 3L10 1" stroke="#fff" stroke-width="2" fill="none"/></svg></span>Construction</li>
    <li><span class="tick"><svg width="11" height="9" viewBox="0 0 11 9"><path d="M1 4.5l3 3L10 1" stroke="#fff" stroke-width="2" fill="none"/></svg></span>Property development</li>
    <li><span class="tick"><svg width="11" height="9" viewBox="0 0 11 9"><path d="M1 4.5l3 3L10 1" stroke="#fff" stroke-width="2" fill="none"/></svg></span>Demolition</li>
    <li><span class="tick"><svg width="11" height="9" viewBox="0 0 11 9"><path d="M1 4.5l3 3L10 1" stroke="#fff" stroke-width="2" fill="none"/></svg></span>Mining</li>
    <li><span class="tick"><svg width="11" height="9" viewBox="0 0 11 9"><path d="M1 4.5l3 3L10 1" stroke="#fff" stroke-width="2" fill="none"/></svg></span>TransportManufacturing of concrete bricks and blocks</li>
    <li><span class="tick"><svg width="11" height="9" viewBox="0 0 11 9"><path d="M1 4.5l3 3L10 1" stroke="#fff" stroke-width="2" fill="none"/></svg></span>Lightweight concrete Readymix</li>
  </ul>
</section>

<div class="stitle" style="top:1754px">
  <div class="box" style="left:467px;top:0;width:258px;height:57px"></div>
  <h2 style="top:16px">OUR <span class="blue">NEWS</span></h2>
  <div class="rule" style="top:69px"><i class="l"></i><i class="sq"></i><i class="sq k"></i><i class="sq"></i><i class="l"></i></div>
</div>
<p class="lead" style="top:1847px">Lorem Ipsum is simply dummy text of the printing and typesetting industry. Lorem Ipsum has been the industry's standard dummy text ever since the.Lorem Ipsum is simply dummy text of the printing and typesetting industry. Lorem Ipsum has been the industry's standard dummy text ever since the. Lorem Ipsum is simply dummy text of the printing and typesetting industry. Lorem Ipsum has been the industry's standard dummy text ever since the.Lorem Ipsum is simply dummy.</p>

<article class="card" style="left:173px">
  <div class="thumb t1" role="img" aria-label="Excavators working on a demolition site"></div>
  <div class="date"><b>18</b><span>DEC</span></div>
  <h3>There are many variations of passages of Lorem Ipsumvailable</h3>
  <p>Lorem Ipsum is simply dummy text of the printing and typesetting industry. Lorem Ipsum has been the industry's standard dummy text ever since the 1500s, when an unknown printer took.</p>
</article>
<article class="card" style="left:466px">
  <div class="thumb t2" role="img" aria-label="Team of workers in hard hats on a building site"></div>
  <div class="date"><b>17</b><span>DEC</span></div>
  <h3>There are many variations of passages of Lorem Ipsumvailable</h3>
  <p>Lorem Ipsum is simply dummy text of the printing and typesetting industry. Lorem Ipsum has been the industry's standard dummy text ever since the 1500s, when an unknown printer took.</p>
</article>
<article class="card" style="left:759px">
  <div class="thumb t3" role="img" aria-label="Forklift loading a truck at a warehouse"></div>
  <div class="date"><b>16</b><span>DEC</span></div>
  <h3>There are many variations of passages of Lorem Ipsumvailable</h3>
  <p>Lorem Ipsum is simply dummy text of the printing and typesetting industry. Lorem Ipsum has been the industry's standard dummy text ever since the 1500s, when an unknown printer took.</p>
</article>

<section class="contact" role="img" aria-label="City skyline at dusk, darkened">
  <div class="stitle dark" style="top:30px">
    <div class="box" style="left:392px;top:0;width:406px;height:57px"></div>
    <h2 style="top:16px">CONTACT <span class="blue">US NOW</span></h2>
    <div class="rule" style="top:69px"><i class="l"></i><i class="sq"></i><i class="sq k"></i><i class="sq"></i><i class="l"></i></div>
  </div>
  <div class="phone-line"><span class="blue">+ 27 (0) 41 308 7724</span> CALL US 24 HOURS / 7 DAYS</div>
  <p class="lead" style="left:240px;width:720px">Lorem Ipsum is simply dummy text of the printing and typesetting industry. Lorem Ipsum has been the industry's standard dummy text ever since the.Lorem Ipsum is simply dummy text of the printing and typesetting industry. Lorem Ipsum has been the industry's standard dummy text ever since the.</p>
  <div class="field" style="left:173px;top:275px;width:415px">First Name</div>
  <div class="field" style="left:612px;top:275px;width:415px">Last Name</div>
  <div class="field" style="left:173px;top:330px;width:415px">Phone Number</div>
  <div class="field" style="left:612px;top:330px;width:415px">E-Mail</div>
  <div class="field" style="left:173px;top:385px;width:854px;height:96px">Message</div>
  <div class="btn">SUBMIT NOW</div>
</section>

<footer class="footer">
  <span class="copy">© 2018 VORLANE . ALL RIGHT RESERVED.</span>
  <div class="social" style="left:898px;top:15px;gap:6px"><span></span><span></span><span></span><span></span></div>
</footer>

</body>
</html>
```